Velmo BUSINESS CARD

Design an attention-grabbing business cards. Draw inspiration from the provided logo file. Please use the same font style as in the logo.
the back side of the card is for accent/decoration.

Contact Information for Business Card

PLEASE USE PROVIDED BUSINESS CARD SAMPLE

Other font styles liked:
• LUMETTE

Colors
EB3D1F
EC4F4E
F09395
F8D3D4
FCEDEE

Requirements
Must have
• RED, BLACK COLORS, SOLID BACK COLOR
Nice to have
• MAKE IT FANCY

```html
<!DOCTYPE html>
<html lang="en">
<head>
<meta charset="utf-8">
<title>Velmo Business Card</title>
<link rel="stylesheet" href="https://fonts.googleapis.com/css2?family=Audiowide&family=Mulish:wght@400;600&display=swap">
<style>
  :root {
    --page: #e9e6e2;
    --card: #1f1e1f;
    --white: #ffffff;
    --red: #eb3d1f;
    --red-soft: #ec4f4e;
    --grey-text: #c9c9c9;
    --rule: #4a494b;
    --emblem-tone: #2a292b;
  }
  * { box-sizing: border-box; margin: 0; padding: 0; }
  html, body { width: 1200px; height: 900px; overflow: hidden; }
  body {
    background: var(--page);
    font-family: "Mulish", Arial, sans-serif;
    position: relative;
  }
  .card {
    position: absolute;
    left: 285px;
    width: 630px;
    height: 360px;
    background: var(--card);
    overflow: hidden;
    box-shadow: 0 10px 28px rgba(0,0,0,.28);
  }
  .card--front { top: 45px; }
  .card--back { top: 495px; }

  .emblem-decoration {
    position: absolute;
    border-radius: 50%;
    background: radial-gradient(circle at 50% 50%, var(--emblem-tone) 0%, rgba(42,41,43,.6) 55%, rgba(31,30,31,0) 72%);
  }
  .card--front .emblem-decoration { left: 20px; top: 150px; width: 300px; height: 300px; }
  .card--back .emblem-decoration { left: 70px; top: 150px; width: 320px; height: 320px; }

  .brand { position: absolute; display: flex; align-items: center; gap: 16px; }
  .brand__square { width: 64px; height: 64px; background: var(--white); flex: none; }
  .brand__text { display: flex; flex-direction: column; }
  .brand__name {
    font-family: "Audiowide", Arial, sans-serif;
    color: var(--white);
    font-size: 66px;
    line-height: 1;
    letter-spacing: 2px;
  }
  .brand__tagline {
    font-family: "Mulish", Arial, sans-serif;
    color: var(--grey-text);
    font-size: 12px;
    letter-spacing: 1.5px;
    margin-top: 6px;
    margin-left: 4px;
  }
  .card--front .brand { left: 150px; top: 60px; }

  .card--back .brand { right: 36px; bottom: 44px; }
  .card--back .brand__square { width: 54px; height: 54px; }
  .card--back .brand__name { font-size: 54px; }
  .card--back .brand__tagline { font-size: 10.5px; }

  .person { position: absolute; left: 36px; top: 70px; }
  .person__role { color: var(--grey-text); font-size: 15px; }
  .person__name {
    font-family: "Audiowide", Arial, sans-serif;
    color: var(--red);
    font-size: 22px;
    letter-spacing: 1px;
    margin: 2px 0 6px;
  }
  .person__mobile { display: flex; align-items: center; gap: 10px; color: var(--grey-text); font-size: 15px; }

  .contact-list { position: absolute; left: 300px; top: 48px; list-style: none; }
  .contact-list li {
    display: flex; align-items: center; gap: 10px;
    color: var(--grey-text); font-size: 14.5px; margin-bottom: 7px;
  }
  .icon { width: 14px; height: 14px; flex: none; }
  .icon path, .icon rect, .icon circle { fill: var(--red-soft); }
  .icon--outline rect { fill: none; stroke: var(--red-soft); stroke-width: 1.5; }

  .divider { position: absolute; left: 300px; right: 0; top: 180px; height: 1px; background: var(--rule); }
</style>
</head>
<body>

<section class="card card--front" aria-label="Card front">
  <div class="emblem-decoration" role="img" aria-label="Faint brand emblem decoration"></div>
  <div class="brand">
    <div class="brand__square"></div>
    <div class="brand__text">
      <span class="brand__name">VELMO</span>
      <span class="brand__tagline">LOGISTICS, REFORGED</span>
    </div>
  </div>
</section>

<section class="card card--back" aria-label="Card back">
  <div class="emblem-decoration" role="img" aria-label="Faint brand emblem decoration"></div>

  <div class="person">
    <p class="person__role">President</p>
    <p class="person__name">NOLAN REYES</p>
    <p class="person__mobile">
      <svg class="icon icon--outline" viewBox="0 0 14 14"><rect x="3.5" y="1" width="7" height="12" rx="1.2"/></svg>
      +317-582-1904
    </p>
  </div>

  <ul class="contact-list">
    <li>
      <svg class="icon" viewBox="0 0 14 14"><path d="M3 1.5l2.5 2.6-1.3 1.6c.8 1.7 2 2.9 3.7 3.7l1.6-1.3 2.6 2.5-1.6 2C5.5 12.2 1.8 8.5 1 3.1z"/></svg>
      +317-730-4418
    </li>
    <li>
      <svg class="icon" viewBox="0 0 14 14"><path d="M1 3h12v8H1z"/></svg>
      NReyes@velmo-llc.com
    </li>
    <li>
      <svg class="icon" viewBox="0 0 14 14"><circle cx="7" cy="7" r="6"/></svg>
      www.Velmo-LLC.com
    </li>
    <li>
      <svg class="icon" viewBox="0 0 14 14"><path d="M7 0.5a4.5 4.5 0 0 0-4.5 4.5C2.5 8.4 7 13.5 7 13.5S11.5 8.4 11.5 5A4.5 4.5 0 0 0 7 .5zm0 6.3a1.8 1.8 0 1 1 0-3.6 1.8 1.8 0 0 1 0 3.6z"/></svg>
      1842 N.250 East. Brookdale, IN, 46020
    </li>
  </ul>

  <div class="divider"></div>

  <div class="brand">
    <div class="brand__square"></div>
    <div class="brand__text">
      <span class="brand__name">VELMO</span>
      <span class="brand__tagline">LOGISTICS, REFORGED</span>
    </div>
  </div>
</section>

</body>
</html>
```